"Every Lantern Still Burning" Sermon Series Design

Needing a design for our church's next sermon series titled "Every Lantern Still Burning" where we will discuss the need for unity, diversity, love and clarity. Looking for a 1920 x 1080 (or higher res) editable and layered file (PSD or AI) so that we can reformat the design to work on social, screens, lower thirds and various print and online mediums. We will also need to have access to the font files so that we can make resize and tweak as needed. We like the idea of using a globe or map of the world as the backdrop with the words overtop. Or, the idea of creating a bunch of newspaper clippings (generic, so that they can't actually be read) and making the shape of a heart. See attached examples. This website will give you an idea of our previous sermon series designs so you can have an idea of our style (but, feel free to help us advance the ball on something more aligned with current design trends): https://www.brinmoorfellowship.church/series

Examples use red, but stay away from a ton of red. If you're gonna major in a color, use blue or something in that family.

Must haves:
Title: Every Lantern Still Burning
Tagline : (TBD - use some Lorem Ipsum as a placeholder and we will fill in later)
Our Logo (attached) (small towards bottom is standard - only use solid colors for logo - preferably just solid black or white)

Industry/Entity Type

Church

Font styles to use
Serif
Sans Serif

Requirements
Must have
• Title: Every Lantern Still Burning
Nice to have
• We like the idea of using a globe or map of the world as the backdrop with the words overtop. Or, the idea of creating a bunch of newspaper clippings (generic, so that they can't actually be read) and making the shape of a heart. See attached examples.

If you're gonna major on a color, stick with blue or something close.
Should not have
• Don't use red as the primary color (example we sent has red, but stay away from it)

```html
<!DOCTYPE html>
<html lang="en">
<head>
<meta charset="utf-8">
<title>Every Lantern Still Burning</title>
<link href="https://fonts.googleapis.com/css2?family=Barlow+Condensed:wght@500;600&display=swap" rel="stylesheet">
<style>
  :root {
    --blue: #1770e6;
    --blue-deep: #0a3fa8;
    --navy: #061a44;
    --white: #ffffff;
    --red: #f20c12;
  }
  * { margin: 0; padding: 0; box-sizing: border-box; }
  html, body { width: 1200px; height: 675px; overflow: hidden; background: var(--blue); }
  .series-art {
    position: relative;
    width: 1200px;
    height: 675px;
    overflow: hidden;
    font-family: "Barlow Condensed", "Arial Narrow", sans-serif;
  }
  .collage-backdrop {
    position: absolute;
    inset: 0;
    background: linear-gradient(135deg, #1b78ee 0%, var(--blue) 50%, #1266d8 100%);
  }
  .globe {
    position: absolute;
    left: 268px;
    top: 10px;
    width: 664px;
    height: 664px;
    border-radius: 50%;
    background: radial-gradient(circle at 45% 40%, #2a63c4 0%, #133d8f 45%, var(--navy) 80%, #030e28 100%);
  }
  .title {
    position: absolute;
    left: 0;
    right: 0;
    top: 175px;
    text-align: center;
    color: var(--white);
    font-weight: 600;
    font-size: 185px;
    line-height: 156px;
    letter-spacing: -1px;
    text-transform: uppercase;
  }
  .title-line { display: block; white-space: nowrap; }
  .heart-badge {
    display: inline-block;
    width: 134px;
    height: 134px;
    margin: 0 12px;
    vertical-align: -2px;
  }
  .tagline {
    position: absolute;
    left: 252px;
    top: 505px;
    width: 696px;
    height: 52px;
    background: var(--white);
    color: var(--blue);
    font-weight: 600;
    font-size: 31px;
    letter-spacing: -0.4px;
    line-height: 52px;
    text-align: center;
    text-transform: uppercase;
    white-space: nowrap;
    overflow: hidden;
  }
  .church-mark {
    position: absolute;
    right: 22px;
    bottom: 34px;
    display: flex;
    align-items: center;
    gap: 10px;
    color: var(--white);
    font-weight: 600;
    font-size: 22px;
    text-transform: uppercase;
    letter-spacing: 1px;
  }
  .church-mark-dot {
    width: 18px;
    height: 18px;
    border: 3px solid var(--white);
    border-radius: 50%;
  }
</style>
</head>
<body>
  <main class="series-art">
    <div class="collage-backdrop" role="img" aria-label="Blue-tinted collage of overlapping newspaper front pages"></div>
    <div class="globe" role="img" aria-label="Satellite view of planet Earth with white cloud swirls, tinted dark blue"></div>

    <h1 class="title">
      <span class="title-line">Every Lantern</span>
      <span class="title-line">Still<svg class="heart-badge" viewBox="0 0 100 100" aria-hidden="true"><circle cx="50" cy="50" r="50" fill="#f20c12"/><path d="M50 78 C30 62 20 52 20 39 C20 29 28 22 37 22 C43 22 47 25 50 30 C53 25 57 22 63 22 C72 22 80 29 80 39 C80 52 70 62 50 78 Z" fill="#ffffff"/></svg>Burning</span>
    </h1>

    <p class="tagline">The immediate need for unity, diversity, love and clarity</p>

    <div class="church-mark">
      <span class="church-mark-dot"></span>
      <span>Brinmoor Fellowship</span>
    </div>
  </main>
</body>
</html>
```